Commerical Office Furniture Company Needs Truck Wrap Design for Box Truck

We need a truck wrap design (and business card) for our company based in Fresno, California. We offer commercial office furnishings such as private office desks, cubicle stations, conference tables, all office seating (task chairs, guest, lobby/lounge, conference) storage systems, ergonomic solutions (monitor arms, keyboard trays, lift desks) and much more. We are a full service office furniture dealer who can fully outfit every space and need for a new or existing office space. We also offer design and space planning services and professional installation.
We would like our trap wrap to be modern using the same color scheme as our logo with a clean but eye catching look. Perhaps using a few nice looking desk/workstations product images as examples to show people what we are capable of. We attached some examples of some themes/layouts we like. feel free to be creative. Our website trymoldavo.com has some images and info.
https://photoshelf.brovane-co.com/detail/client-space-shared-tessel-workstation-with-q-line-storage-height-adjustable-tables-and-wexmoor-seating
Target Market(s)
Private Sector, Education, Healthcare
Industry/Entity Type
Requirements
Must have
- Dorvik Box Truck - 190 inches x 85 inches

```html
<!DOCTYPE html>
<html lang="en">
<head>
<meta charset="utf-8">
<title>Moldavo Office Interiors – Box Truck Wrap</title>
<link href="https://fonts.googleapis.com/css2?family=Exo+2:wght@600;700&family=Oswald:wght@500&display=swap" rel="stylesheet">
<style>
  :root {
    --brand-blue: #0a58a3;
    --brand-blue-light: #1f7fd1;
    --icon-blue: #3aa3ec;
    --white: #ffffff;
    --page: #ffffff;
    --photo-dark: #4a4a4f;
    --photo-light: #d9dde2;
  }
  * { margin: 0; padding: 0; box-sizing: border-box; }
  html, body { width: 1200px; height: 616px; overflow: hidden; background: var(--page); }
  .canvas { position: relative; width: 1200px; height: 616px; }

  .panel {
    position: absolute;
    background: radial-gradient(circle at 45% 55%, var(--brand-blue-light), var(--brand-blue) 70%);
    overflow: hidden;
    font-family: "Exo 2", sans-serif;
    color: var(--white);
  }
  .panel-side { left: 262px; top: 152px; width: 474px; height: 210px; }
  .panel-rear { left: 867px; top: 146px; width: 249px; height: 229px; }

  .white-sweep { position: absolute; left: 0; top: 0; }

  .brand-name {
    position: absolute;
    color: var(--brand-blue);
    font-weight: 700;
    text-align: center;
    line-height: 1;
  }
  .brand-name .word { display: block; font-size: 19px; letter-spacing: 1px; }
  .brand-name .sub { display: block; font-size: 7px; letter-spacing: 1.6px; margin-top: 3px; }
  .panel-side .brand-name { left: 18px; top: 30px; width: 100px; }
  .panel-rear .brand-name { left: 14px; top: 22px; width: 96px; }

  .product-photo {
    position: absolute;
    background: linear-gradient(180deg, var(--photo-dark) 0%, #6b5f55 55%, var(--photo-light) 100%);
  }
  .panel-side .product-photo { left: 246px; top: 0; width: 228px; height: 146px; }
  .panel-rear .product-photo { left: 26px; top: 38px; width: 199px; height: 124px; }

  .contact-list { position: absolute; left: 148px; top: 47px; list-style: none; }
  .contact-list li {
    display: flex; align-items: center; gap: 5px;
    font-size: 7.5px; font-weight: 700; line-height: 1.1;
    margin-bottom: 13px;
  }
  .contact-list svg { width: 11px; height: 11px; flex: none; }

  .service-row {
    position: absolute; left: 0; right: 0; top: 164px; height: 38px;
    display: flex; align-items: center;
  }
  .service {
    flex: 1; text-align: center;
    font-family: "Oswald", sans-serif; font-weight: 500;
    font-size: 11.5px; line-height: 1.1; text-transform: uppercase;
  }
  .service + .service { border-left: 1.5px solid var(--white); }

  .rear-contact { position: absolute; left: 0; right: 0; top: 177px; text-align: center; }
  .rear-phone { font-size: 17px; font-weight: 700; display: flex; justify-content: center; align-items: center; gap: 8px; }
  .rear-web { font-size: 10.5px; font-weight: 700; display: flex; justify-content: center; align-items: center; gap: 8px; margin-top: 2px; }
  .rear-phone svg { width: 14px; height: 14px; }
  .rear-web svg { width: 9px; height: 9px; }
</style>
</head>
<body>
<main class="canvas">

  <section class="panel panel-side" aria-label="Truck side panel">
    <svg class="white-sweep" width="474" height="210" viewBox="0 0 474 210">
      <path d="M8 8 H148 C128 40 122 86 82 92 C42 98 16 110 8 135 Z" fill="#ffffff"/>
    </svg>
    <div class="brand-name"><span class="word">MOLDAVO</span><span class="sub">OFFICE INTERIORS</span></div>

    <ul class="contact-list">
      <li>
        <svg viewBox="0 0 12 12"><circle cx="6" cy="6" r="6" fill="var(--icon-blue)"/><path d="M4 3 L5.2 4.6 L4.6 5.3 Q5.4 6.8 6.8 7.4 L7.4 6.8 L9 8 L8.3 9 Q5 9 3 5 Z" fill="#fff"/></svg>
        (555) 014-2763
      </li>
      <li>
        <svg viewBox="0 0 12 12"><circle cx="6" cy="6" r="6" fill="var(--icon-blue)"/><path d="M6 2.5 A2.3 2.3 0 0 1 8.3 4.8 C8.3 6.5 6 9.5 6 9.5 C6 9.5 3.7 6.5 3.7 4.8 A2.3 2.3 0 0 1 6 2.5 Z" fill="#fff"/><circle cx="6" cy="4.8" r="0.9" fill="var(--icon-blue)"/></svg>
        <span>1870 W. Larkspur Ave<br>Fresno, CA 93700</span>
      </li>
      <li>
        <svg viewBox="0 0 12 12"><circle cx="6" cy="6" r="6" fill="var(--icon-blue)"/><path d="M4 3 L8.5 6.5 L6.5 6.8 L7.6 9 L6.8 9.4 L5.7 7.2 L4 8.5 Z" fill="#fff"/></svg>
        www.trymoldavo.com
      </li>
    </ul>

    <div class="product-photo" role="img" aria-label="Product photo: height-adjustable workstation with storage hutch, cabinets and white task chair"></div>

    <div class="service-row">
      <div class="service">Commercial Grade<br>Furniture</div>
      <div class="service">Design &amp; Space<br>Planning</div>
      <div class="service">Free On-Site<br>Consultation</div>
      <div class="service">Professional<br>Install</div>
    </div>
  </section>

  <section class="panel panel-rear" aria-label="Truck rear panel">
    <div class="product-photo" role="img" aria-label="Product photo: height-adjustable workstation with storage hutch, cabinets and white task chair"></div>
    <svg class="white-sweep" width="249" height="229" viewBox="0 0 249 229">
      <path d="M4 4 H155 C136 30 122 68 82 74 C42 80 16 94 4 106 Z" fill="#ffffff"/>
    </svg>
    <div class="brand-name"><span class="word">MOLDAVO</span><span class="sub">OFFICE INTERIORS</span></div>

    <div class="rear-contact">
      <div class="rear-phone">
        <svg viewBox="0 0 12 12"><path d="M2 1 L4.5 4 L3.4 5.3 Q4.8 8 7 8.8 L8.2 7.6 L11 9.8 L9.8 11.5 Q4 11 1 3 Z" fill="var(--icon-blue)"/></svg>
        (555) 014-2763
      </div>
      <div class="rear-web">
        <svg viewBox="0 0 12 12"><path d="M2 1 L10 7 L6.5 7.5 L8.5 11 L7 11.7 L5.2 8.2 L2 10.5 Z" fill="var(--icon-blue)"/></svg>
        www.trymoldavo.com
      </div>
    </div>
  </section>

</main>
</body>
</html>
```